R&T Architects - business card and stationary

Aloha,

We have a simple text logo, we need it incorporated into a business card and also stationary design (letterhead) if possible.

Please check out our website, rtmpacific.com for a little more about us. The logo we would like to use is in the upper left corner of the website. It is a simple colored logo based on the Klavica font. We are open to new logo's as well, but we want simple.

Thanks

```html
<!DOCTYPE html>
<html lang="en">
<head>
<meta charset="utf-8">
<title>R&amp;T Architects – Business Card</title>
<link rel="stylesheet" href="https://fonts.googleapis.com/css2?family=Questrial&family=Source+Sans+3:wght@400;600&display=swap">
<style>
  :root {
    --paper: #ffffff;
    --frame: #2b2b2b;
    --ink-brown: #6b6056;
    --ink-gray: #7a7a7a;
    --accent-olive: #b3a83a;
    --accent-gold: #cdbb2c;
  }
  html, body {
    margin: 0;
    padding: 0;
    width: 1029px;
    height: 1200px;
    overflow: hidden;
    background: var(--paper);
  }
  .sheet {
    position: relative;
    width: 1029px;
    height: 1200px;
  }
  .card {
    position: absolute;
    left: 113px;
    width: 796px;
    height: 466px;
    border: 1.5px solid var(--frame);
    box-sizing: border-box;
    background: var(--paper);
  }
  .card--front { top: 98px; }
  .card--back { top: 633px; }

  .wordmark {
    position: absolute;
    left: 40px;
    bottom: 28px;
    margin: 0;
    font-family: "Source Sans 3", sans-serif;
    font-weight: 600;
    font-size: 70px;
    line-height: 1;
    letter-spacing: -0.5px;
    color: var(--ink-brown);
  }

  .contact-list {
    position: absolute;
    left: 39px;
    top: 34px;
    margin: 0;
    padding: 0;
    list-style: none;
    font-family: "Questrial", sans-serif;
    font-size: 28px;
    line-height: 40px;
    color: var(--ink-gray);
    letter-spacing: 0.4px;
  }
  .contact-list li {
    display: flex;
    white-space: nowrap;
  }
  .contact-label {
    display: inline-block;
    width: 35px;
    color: var(--accent-olive);
  }

  .person-name {
    position: absolute;
    left: 41px;
    bottom: 36px;
    margin: 0;
    font-family: "Source Sans 3", sans-serif;
    font-weight: 400;
    font-size: 42px;
    line-height: 1;
    letter-spacing: -1px;
    color: var(--ink-brown);
  }
  .person-name .initial { color: var(--accent-gold); }
</style>
</head>
<body>
  <main class="sheet">
    <section class="card card--front" aria-label="Card front">
      <h1 class="wordmark">R&amp;T Architects</h1>
    </section>

    <section class="card card--back" aria-label="Card back">
      <ul class="contact-list">
        <li><span class="contact-label">p</span>(808) 555-0147</li>
        <li><span class="contact-label">c</span>(808) 555-0147</li>
        <li><span class="contact-label">a</span>48-2210 Makai Loa Road Waimea, Hawaii 96738</li>
        <li><span class="contact-label">e</span>noah@rtmpacific.com</li>
        <li><span class="contact-label">w</span>rtmpacific.com</li>
      </ul>
      <p class="person-name">Noah<span class="initial">J</span>Palani</p>
    </section>
  </main>
</body>
</html>
```